Pain Seminar Flyer 8.5x11

We are having a FREE seminar on Pain for our Bootcamp members at our gym. We are looking for a great looking flyer with pictures and a design to draw people in. I have attached our logo, pictures of the 2 speakers and a Word document of the flyer information needed. PLEASE PLEASE make our head shots small and in a circle like the example flyer we attached but obviously make the flyer much much nicer than the example. Also we attached pic ideas about pain.
- This must be in PSD. format WITH LAYERS and fonts so we can edit the time or reuse the flyer.
- Size 8.5x11
- Attached info. with pics and logo (along with other pics of pain!)
Thank you!
Gym

```html
<!DOCTYPE html>
<html lang="en">
<head>
<meta charset="utf-8">
<title>Free Pain Seminar Flyer</title>
<link rel="stylesheet" href="https://fonts.googleapis.com/css2?family=Archivo+Black&family=Oswald:wght@500;700&family=Lato:wght@400;700;900&display=swap">
<style>
  :root {
    --sky: #5598dc;
    --copper: #c47f3c;
    --ink: #2b2b2b;
    --charcoal: #3d3d3d;
    --paper: #ffffff;
    --backdrop: #ececec;
    --rule: #e6e6e6;
  }
  * { box-sizing: border-box; margin: 0; padding: 0; }
  html, body { width: 1200px; height: 1200px; overflow: hidden; }
  body { background: var(--backdrop); position: relative; font-family: "Lato", sans-serif; }

  .flyer {
    position: absolute; left: 193px; top: 76px;
    width: 814px; height: 1048px;
    background: var(--paper); overflow: hidden;
  }

  /* pain pills */
  .pain-row { position: absolute; top: 46px; left: 40px; width: 738px; height: 58px; }
  .pain-link { position: absolute; top: 24px; height: 10px; background: var(--sky);
    border-top: 2px solid var(--copper); border-bottom: 2px solid var(--copper); }
  .pain-pill {
    position: absolute; top: 0; height: 58px;
    background: var(--sky); border: 2px solid var(--copper); border-radius: 22px;
    box-shadow: inset 0 0 0 2px #fff;
    color: #fff; font-family: "Oswald", sans-serif; font-weight: 500;
    font-size: 30px; line-height: 54px; text-align: center; letter-spacing: 0.5px;
    white-space: nowrap;
  }

  /* title band */
  .title-band {
    position: absolute; left: 0; top: 144px; width: 814px; height: 144px;
    background: var(--copper); text-align: center; color: #fff;
  }
  .title-band::before, .title-band::after {
    content: ""; position: absolute; left: 0; width: 100%; height: 8px;
    background: repeating-linear-gradient(90deg, var(--paper) 0 6px, transparent 6px 12px);
  }
  .title-band::before { top: 0; }
  .title-band::after { bottom: 0; }
  .title-main { font-family: "Archivo Black", sans-serif; font-size: 60px; line-height: 1;
    padding-top: 18px; letter-spacing: 1px; white-space: nowrap; }
  .title-sub { font-family: "Oswald", sans-serif; font-weight: 700; font-size: 48px;
    line-height: 1; margin-top: 4px; white-space: nowrap; }

  /* date */
  .date-line {
    position: absolute; left: 90px; top: 316px; width: 634px; height: 72px;
    border-top: 1px solid var(--rule); border-bottom: 1px solid var(--rule);
    text-align: center; font-family: "Oswald", sans-serif; font-weight: 700;
    font-size: 42px; line-height: 70px; white-space: nowrap;
  }
  .date-day { color: var(--sky); }
  .date-week { color: var(--copper); margin-left: 14px; }
  .date-time { color: var(--ink); margin-left: 8px; }

  /* topics */
  .topics { position: absolute; left: 0; top: 404px; width: 814px; list-style: none;
    text-align: center; color: var(--ink); font-size: 23px; }
  .topics li { height: 39px; line-height: 39px; white-space: nowrap; }
  .topics li::before { content: ""; display: inline-block; width: 13px; height: 13px;
    border-radius: 50%; background: var(--copper); margin-right: 9px; vertical-align: 2px; }

  /* venue */
  .venue { position: absolute; left: 0; top: 570px; width: 814px; height: 74px;
    background: var(--sky); color: #fff; text-align: center; font-size: 24px; line-height: 30px;
    padding-top: 8px; white-space: nowrap; }

  /* speakers */
  .speaker { position: absolute; top: 656px; width: 236px; height: 220px; }
  .speaker-photo {
    position: absolute; left: 12px; top: 0; width: 212px; height: 212px; border-radius: 50%;
    border: 4px solid var(--sky); padding: 4px; background: var(--paper);
  }
  .speaker-photo span { display: block; width: 100%; height: 100%; border-radius: 50%;
    border: 3px solid var(--copper); }
  .speaker--left .speaker-photo span { background: radial-gradient(circle at 50% 40%, #c7b59a, #6f7d52 70%); }
  .speaker--right .speaker-photo span { background: radial-gradient(circle at 50% 40%, #d8a888, #b9bcc0 70%); }
  .speaker-tab { position: absolute; top: 164px; width: 20px; height: 14px; background: #a96a2f; }
  .speaker-name {
    position: absolute; left: 0; top: 176px; width: 236px; height: 28px;
    background: var(--copper); color: #fff; text-align: center;
    font-size: 15px; line-height: 28px; white-space: nowrap;
  }

  /* brand */
  .brand { position: absolute; left: 0; top: 900px; width: 814px; height: 90px;
    text-align: center; color: var(--ink); font-family: "Lato", sans-serif; font-weight: 900;
    font-size: 32px; line-height: 90px; letter-spacing: 2px; white-space: nowrap; }

  /* footer */
  .footer { position: absolute; left: 0; top: 1002px; width: 814px; height: 30px;
    background: var(--charcoal); color: #fff; text-align: center;
    font-size: 19px; line-height: 30px; letter-spacing: 4px; white-space: nowrap; }
</style>
</head>
<body>
  <main class="flyer">
    <div class="pain-row">
      <div class="pain-link" style="left:200px;width:80px"></div>
      <div class="pain-link" style="left:500px;width:80px"></div>
      <div class="pain-pill" style="left:0;width:204px">BACK PAIN?</div>
      <div class="pain-pill" style="left:234px;width:270px">SHOULDER PAIN?</div>
      <div class="pain-pill" style="left:534px;width:204px">KNEE PAIN?</div>
    </div>

    <header class="title-band">
      <h1 class="title-main">FREE SEMINAR</h1>
      <h2 class="title-sub">ON HOW TO STOP PAIN</h2>
    </header>

    <p class="date-line">
      <span class="date-day">13th APRIL</span><span class="date-week">THURSDAY,</span><span class="date-time">7:30PM-9PM</span>
    </p>

    <ul class="topics">
      <li>How to Get Out of Pain</li>
      <li>What to do When an Exercise Hurts</li>
      <li>How Exercise Helps Pain</li>
      <li>Q &amp; A to Fine Extraordinary Health</li>
    </ul>

    <section class="venue">
      <p>MOTIVRA PERSONAL TRAINING STUDIO</p>
      <p>214 ELM ST. WESTFIELD, CO 80999</p>
    </section>

    <figure class="speaker speaker--left" style="left:60px">
      <div class="speaker-photo"><span role="img" aria-label="Headshot of speaker Daniel Marsh"></span></div>
      <div class="speaker-tab" style="left:-2px"></div>
      <div class="speaker-tab" style="right:-2px"></div>
      <figcaption class="speaker-name">DANIEL MARSH, PT, DPT, OCS</figcaption>
    </figure>

    <figure class="speaker speaker--right" style="left:479px">
      <div class="speaker-photo"><span role="img" aria-label="Headshot of speaker Corey Hale"></span></div>
      <div class="speaker-tab" style="left:-2px"></div>
      <div class="speaker-tab" style="right:-2px"></div>
      <figcaption class="speaker-name">COREY HALE, MS, CSCS, FMS</figcaption>
    </figure>

    <div class="brand">MOTIVRA BOOTCAMPS</div>

    <footer class="footer">www.motivrafit.com</footer>
  </main>
</body>
</html>
```